Business Card for Vorlo Parts Wholesale supplier

Hi There! I need a new business card for our company. We are specialized in selling Vorlo parts, mostly we sell new LCD screens for uDialr and oTabs. I would like to see that back in the design.

You can find the colors and logo's on our website: www.darvok.nl

Industry/Entity Type

Business

Contact Information for Business Card

My Details:
Bas Hollink

Phone: 0031627381946
E-mail: Bas@darvok.nl

Slogan: "Because Quality Matters"

Font styles to use
Sans Serif

Colors

Designer to choose colors to be used in the design.

Requirements
Must have
• A Black backside with the Darvok logo on it. The front side should be clean with only my contact details.
• But I'm also open for something really different or awesome!
Nice to have
• Remember that we are in the parts & repairing industry, So i'll be handing those business cards mainly to repair companies. Maybe you can do something with that thought :)

```html
<!DOCTYPE html>
<html lang="en">
<head>
<meta charset="utf-8">
<title>Darvok Business Card</title>
<link href="https://fonts.googleapis.com/css2?family=Exo+2:wght@600;700;800&family=Dancing+Script:wght@500&display=swap" rel="stylesheet">
<style>
  :root {
    --stage: #1c1c1c;
    --ink: #0b0b0b;
    --paper: #ffffff;
    --orange: #f47a20;
    --white: #ffffff;
    --muted: #d9d9d9;
  }
  * { margin: 0; padding: 0; box-sizing: border-box; }
  html, body { width: 1200px; height: 852px; overflow: hidden; }
  body {
    background: var(--stage);
    font-family: "Exo 2", Arial, sans-serif;
    position: relative;
  }
  .card {
    position: absolute;
    width: 560px;
    height: 320px;
    border-radius: 18px;
    overflow: hidden;
    box-shadow: 0 14px 30px rgba(0,0,0,.55);
  }
  /* Back side */
  .card--back {
    left: 60px; top: 90px;
    background: var(--ink);
  }
  .back__brand {
    position: absolute;
    left: 0; right: 0; top: 112px;
    display: flex; align-items: center; justify-content: center; gap: 16px;
  }
  .brand__square {
    width: 44px; height: 44px;
    background: var(--orange);
  }
  .brand__name {
    font-weight: 800;
    font-size: 68px;
    line-height: 1;
    color: var(--white);
    letter-spacing: 1px;
  }
  .back__tagline {
    position: absolute;
    left: 0; right: 0; bottom: 46px;
    text-align: center;
    font-weight: 800;
    font-size: 17px;
    letter-spacing: 2px;
    text-transform: uppercase;
    color: var(--white);
  }
  .back__tagline .accent { color: var(--orange); }

  /* Front side */
  .card--front {
    left: 580px; top: 440px;
    background: var(--paper);
  }
  .front__accent {
    position: absolute;
    left: -150px; bottom: -170px;
    width: 380px; height: 380px;
    border-radius: 50%;
    background: var(--orange);
  }
  .front__info {
    position: absolute;
    left: 262px; top: 52px;
  }
  .front__name {
    font-weight: 800;
    font-size: 56px;
    line-height: 1;
    color: var(--ink);
    letter-spacing: 1px;
  }
  .front__slogan {
    font-family: "Dancing Script", cursive;
    font-size: 25px;
    color: var(--orange);
    margin: 2px 0 14px 6px;
  }
  .front__person {
    font-weight: 800;
    font-size: 19px;
    text-transform: uppercase;
    color: var(--ink);
    margin-bottom: 8px;
  }
  .front__person .first { color: var(--orange); }
  .contact-list { list-style: none; }
  .contact-list li {
    display: flex; align-items: center; gap: 9px;
    font-weight: 600;
    font-size: 17px;
    color: var(--ink);
    margin-bottom: 5px;
  }
  .contact-icon {
    width: 18px; height: 18px;
    border-radius: 3px;
    background: var(--ink);
    display: flex; align-items: center; justify-content: center;
    flex: none;
  }
  .contact-icon svg { width: 12px; height: 12px; }
</style>
</head>
<body>

  <section class="card card--back">
    <div class="back__brand">
      <span class="brand__square"></span>
      <span class="brand__name">darvok</span>
    </div>
    <p class="back__tagline"><span class="accent">Specialized in</span> selling Vorlo parts</p>
  </section>

  <section class="card card--front">
    <div class="front__accent"></div>
    <div class="front__info">
      <div class="front__name">darvok</div>
      <div class="front__slogan">Because Quality Matters</div>
      <div class="front__person"><span class="first">Bas</span> Hollink</div>
      <ul class="contact-list">
        <li>
          <span class="contact-icon">
            <svg viewBox="0 0 12 12" fill="none" stroke="#f47a20" stroke-width="1.2">
              <circle cx="6" cy="6" r="5"/><ellipse cx="6" cy="6" rx="2.2" ry="5"/><line x1="1" y1="6" x2="11" y2="6"/>
            </svg>
          </span>
          www.darvok.nl
        </li>
        <li>
          <span class="contact-icon">
            <svg viewBox="0 0 12 12" fill="#f47a20">
              <path d="M2.5 1h2l1 2.8-1.3 1a6.5 6.5 0 0 0 3 3l1-1.3L11 7.5v2c0 .8-.7 1.5-1.5 1.5A8.5 8.5 0 0 1 1 2.5C1 1.7 1.7 1 2.5 1z"/>
            </svg>
          </span>
          0031627381946
        </li>
        <li>
          <span class="contact-icon">
            <svg viewBox="0 0 12 12" fill="none" stroke="#f47a20" stroke-width="1.2">
              <rect x="1" y="2.5" width="10" height="7" rx="1"/><path d="M1.5 3l4.5 3.5L10.5 3"/>
            </svg>
          </span>
          Bas@darvok.nl
        </li>
      </ul>
    </div>
  </section>

</body>
</html>
```